Design and Renovation Company Luxury Business Card

I want to create a luxury business card for a Design and Renovation Firm . We will use our current logo. The company name is 742BUILD. We do not want anything standard. We need a very unique concept.
Please see uploaded inspiration. I really like the textured paper option. I would like the card to be thick with debossing, and/or embossing options. The logo has orange in it but I would like to see the card with and without the orange. I think the orange may make the company feel less high-end. The goal is to elevate the logo not match its vibe per se of the logo. We want something very unique, not standard at all!
I would like a space for :
Logo,
Name,
Position,
Email,
Office number,
Website Address,
Business Address,
Thank you!
Have fun!
Target Market(s)
Home owners Age 35 +
Industry/Entity Type
Design and Renovation
Contact Information for Business Card
Logo, Name, Position, Email, Office number, Website Address, Business Address,.
Colors
Designer to choose colors to be used in the design.
Requirements
Must have
- A luxury designer feel. Must be black or dark grey but open to other luxury ideas.
Nice to have
- Gold, silver, black embossing or debossing. Textured paper design.
Should not have
- A cheap look and feel.

```html
<!DOCTYPE html>
<html lang="en">
<head>
<meta charset="utf-8">
<title>742BUILD Business Card</title>
<link href="https://fonts.googleapis.com/css2?family=Lato:wght@400;700&display=swap" rel="stylesheet">
<style>
  :root {
    --backdrop: #2b2b2b;
    --card: #1c1c1c;
    --card-front: #1f1f1f;
    --deboss: #141414;
    --orange: #f0901e;
    --white: #f4f4f4;
  }
  * { margin: 0; padding: 0; box-sizing: border-box; }
  html, body { width: 1200px; height: 689px; overflow: hidden; }
  body {
    background: var(--backdrop);
    font-family: "Lato", Arial, sans-serif;
    position: relative;
  }
  .card {
    position: absolute;
    top: 196px;
    width: 525px;
    height: 300px;
    overflow: hidden;
  }
  .card--front { left: 45px; background: var(--card-front); border-radius: 4px; }
  .card--back { left: 630px; background: var(--card); border-radius: 14px; }

  .front-wordmark {
    position: absolute;
    inset: 0;
    display: flex;
    align-items: center;
    justify-content: center;
    font-weight: 400;
    font-size: 62px;
    letter-spacing: 6px;
    color: var(--deboss);
  }

  .brand-name {
    position: absolute;
    right: 40px;
    top: 38px;
    font-weight: 400;
    font-size: 40px;
    letter-spacing: 4px;
    line-height: 1;
    color: var(--white);
  }

  .person {
    position: absolute;
    left: 36px;
    top: 132px;
  }
  .person__name {
    font-size: 22px;
    font-weight: 700;
    color: var(--orange);
    letter-spacing: 0.5px;
    line-height: 26px;
  }
  .person__role { font-size: 14px; line-height: 18px; color: var(--white); margin-top: 2px; }

  .divider {
    position: absolute;
    left: 36px;
    right: 40px;
    top: 186px;
    height: 1px;
    background: var(--orange);
  }

  .address {
    position: absolute;
    right: 40px;
    top: 200px;
    text-align: right;
    font-style: normal;
    font-size: 14px;
    line-height: 20px;
    color: var(--white);
  }

  .contacts {
    position: absolute;
    left: 36px;
    top: 200px;
    list-style: none;
  }
  .contacts__item {
    display: flex;
    align-items: center;
    gap: 10px;
    font-size: 14px;
    line-height: 24px;
    color: var(--white);
  }
  .contacts__icon { width: 14px; height: 14px; flex: none; }
</style>
</head>
<body>
  <section class="card card--front" aria-label="Card front">
    <div class="front-wordmark">742BUILD</div>
  </section>

  <section class="card card--back" aria-label="Card back">
    <div class="brand-name">742BUILD</div>

    <div class="person">
      <div class="person__name">MARCUS HALE</div>
      <div class="person__role">Owner</div>
    </div>

    <div class="divider"></div>

    <ul class="contacts">
      <li class="contacts__item">
        <svg class="contacts__icon" viewBox="0 0 16 16" aria-hidden="true">
          <path fill="var(--orange)" d="M3.6 1.2l2.3 2.6-1.3 1.9c.9 2 2.6 3.7 4.6 4.6l1.9-1.3 2.6 2.3-1.4 2.4C6.5 13.6 2.4 9.5 1.2 3.7z"/>
        </svg>
        044-555 019 284
      </li>
      <li class="contacts__item">
        <svg class="contacts__icon" viewBox="0 0 16 16" aria-hidden="true">
          <rect x="1" y="3" width="14" height="10" fill="var(--orange)"/>
          <path d="M1.5 3.5L8 9l6.5-5.5" fill="none" stroke="var(--card)" stroke-width="1.4"/>
        </svg>
        hello@742build.com
      </li>
      <li class="contacts__item">
        <svg class="contacts__icon" viewBox="0 0 16 16" aria-hidden="true">
          <circle cx="8" cy="8" r="6.5" fill="none" stroke="var(--orange)" stroke-width="1.5"/>
          <ellipse cx="8" cy="8" rx="2.6" ry="6.5" fill="none" stroke="var(--orange)" stroke-width="1.2"/>
          <path d="M1.5 8h13" stroke="var(--orange)" stroke-width="1.2"/>
        </svg>
        www.742build.com
      </li>
    </ul>

    <address class="address">
      58 Harbor Row,<br>
      Westfield 20918,<br>
      Avonmere
    </address>
  </section>
</body>
</html>
```